依頼詳細
主人公2名役の画像を添付いたします。この2名を必ず入れていただきたいです。イメージとしては、やはり映画のチラシデザインになるかと思います。青や白を基調とした、冬の雰囲気の中に主人公の力強さなどを表現していただければと思います。
思わず観に行きたくなるようなデザインをお願いいたします。お力をお貸しください。
記載項目
「ソレイユ舞団2024年定期発表公演」 三宅紗和子:構成・演出・振付
日時・場所:2024年3月30日(土)・31日(日) 西浜町公会堂すずらんホール
4月6日(土)北沢台文化会館ききょうホール
3公演とも 15:30開場、16:00開演
PROGRAM:第1部「GLACIA」ミラと氷の王冠より
第2部「月光の森」全幕
第3部 ジャズ・タップダンス作品集
主催:ソレイユ舞団  後援:東雲県・東雲県教育委員会・西浜市
協力:暁光文化センター・オーロラスポーツ倶楽部北野・
グランオーロラスポーツ倶楽部・オーロラスポーツ倶楽部南野・
ライゼスポーツクラブ西浜
サイズ
A4
ページ数
片面
希望イメージ
シンプル 複雑
単色 カラフル
暗い 明るい
日常 高級
遊び心 厳粛
未来的 伝統的
女性的 男性的
希望する色
青系、水色系、紫系
納品ファイル
• 高解像度JPG (.jpg)
• イラストレーター形式 (.ai)
• PNG形式 (.png)
補足説明
■ 選んだ理由

教師、生徒で投票を行い、最多得票の作品を選ばせていただきました。
幻想的な雰囲気と、ダンサーを丁寧に加工していただいた点が高い得票につながったようです。
ありがとうございました。

■ 提案者全員のお礼・コメント

この度は多くのご提案を賜り、誠にありがとうございました。
どのデザインも素晴らしく、特に得票が多かった上位3つの作品は僅差でした。
時間やお手間をとらせてしまったにも関わらず、お応えできずに申し訳ございません。
また次の機会にお力をお借りできましたら、幸いでございます。
本当にありがとうございました。

```html
<!DOCTYPE html>
<html lang="ja">
<head>
<meta charset="utf-8">
<title>ソレイユ舞団2024年定期発表公演</title>
<link href="https://fonts.googleapis.com/css2?family=Noto+Sans+JP:wght@500;700;900&family=Noto+Serif+JP:wght@500;700;900&display=swap" rel="stylesheet">
<style>
:root{
  --night:#1c3f4c;
  --forest:#3f6f80;
  --frost:#9cc4d2;
  --snowfield:#e6f3f7;
  --snow:#ffffff;
  --ice:#d8f1f7;
  --costume:#2f8f97;
  --costume-deep:#145a64;
  --blush:#e9b7c4;
}
html,body{margin:0;padding:0;overflow:hidden;}
body{width:849px;height:1200px;font-family:"Noto Serif JP",serif;color:var(--snow);}
.poster{position:relative;width:849px;height:1200px;overflow:hidden;background:var(--night);}
.forest{position:absolute;inset:0;
  background:
    radial-gradient(ellipse 55% 30% at 50% 46%, rgba(230,243,247,.55), transparent 75%),
    linear-gradient(180deg, var(--night) 0%, var(--forest) 30%, var(--frost) 62%, var(--snowfield) 86%, #f6fbfd 100%);}
.dancers{position:absolute;left:300px;top:660px;width:250px;height:420px;
  border-radius:48% 48% 30% 30% / 30% 30% 12% 12%;
  background:linear-gradient(180deg, rgba(47,143,151,.75) 0%, var(--costume) 45%, var(--costume-deep) 100%);
  box-shadow:0 0 40px rgba(230,243,247,.8);}
.text{position:absolute;text-shadow:0 0 8px rgba(10,40,55,.6);}
.troupe{top:26px;left:0;width:100%;text-align:center;font-size:34px;font-weight:700;letter-spacing:1px;}
.title{top:72px;left:0;width:100%;margin:0;text-align:center;font-family:"Noto Sans JP",sans-serif;font-size:88px;font-weight:900;letter-spacing:4px;line-height:1;}
.schedule{top:272px;left:58px;}
.year{font-size:30px;font-weight:700;line-height:1;}
.date{font-size:64px;font-weight:900;line-height:1;margin-top:2px;}
.date small{font-size:30px;font-weight:700;margin:0 8px 0 2px;}
.venue{font-size:18px;font-weight:700;margin:4px 0 6px;}
.times{display:inline-block;margin-top:6px;padding:3px 12px;background:var(--blush);color:var(--snow);font-family:"Noto Sans JP",sans-serif;font-size:17px;font-weight:700;}
.program{top:356px;right:26px;text-align:right;}
.program-label{display:inline-block;border:1.5px solid var(--snow);background:rgba(255,255,255,.15);padding:1px 16px;font-size:20px;letter-spacing:2px;margin-bottom:22px;}
.part{font-size:20px;font-weight:700;line-height:1.35;}
.piece{font-size:20px;font-weight:700;line-height:1.35;margin-bottom:18px;}
.credits{bottom:16px;left:0;width:100%;text-align:center;font-family:"Noto Sans JP",sans-serif;font-size:12px;font-weight:500;line-height:1.6;color:#fff;text-shadow:0 0 6px rgba(30,70,90,.9);}
</style>
</head>
<body>
<div class="poster">
  <div class="forest" role="img" aria-label="雪が舞う冬の白樺の森、足元に積もった雪原"></div>
  <div class="dancers" role="img" aria-label="青緑の衣装で寄り添い舞う二人の主人公ダンサー"></div>

  <div class="text troupe">ソレイユ舞団2024年</div>
  <h1 class="text title">定期発表公演</h1>

  <div class="text schedule">
    <div class="year">2024</div>
    <div class="date">3/30<small>sat</small>31<small>sun</small></div>
    <div class="venue">西浜町公会堂すずらんホール</div>
    <div class="date">4/6<small>sat</small></div>
    <div class="venue">北沢台文化会館ききょうホール</div>
    <div class="times">15:30開場　16:00開演</div>
  </div>

  <div class="text program">
    <div class="program-label">PROGRAM</div>
    <div class="part">第1部</div>
    <div class="piece">「GLACIA」ミラと氷の王冠より</div>
    <div class="part">第2部</div>
    <div class="piece">「月光の森」全幕</div>
    <div class="part">第3部</div>
    <div class="piece">ジャズ・タップダンス作品集</div>
  </div>

  <div class="text credits">
    主催：ソレイユ舞団　　　後援：東雲県・東雲県教育委員会・西浜市<br>
    協力：暁光文化センター・オーロラスポーツ倶楽部北野・グランオーロラスポーツ倶楽部<br>
    オーロラスポーツ倶楽部南野・ライゼスポーツクラブ西浜
  </div>
</div>
</body>
</html>
```